Create website design - Hire business

Build website to specification. Look and feel only or include all functionality. I have put together a google document which includes all information on requirements. I will share this with you via message once you have been assigned the job.

Coding

Coded - Design and coding required

Number of Pages Required

1 page

Requirements
Must have
• As per Google Doc
Nice to have
• As per Google Doc
Should not have
• As per Google Doc

```html
<!DOCTYPE html>
<html lang="en">
<head>
<meta charset="utf-8">
<title>Over Fence Hire</title>
<link href="https://fonts.googleapis.com/css2?family=Poppins:wght@400;500;600;700&family=Barlow:wght@400;500;600&display=swap" rel="stylesheet">
<style>
:root{
  --blue:#2a7bc8;
  --blue-dark:#1f68ae;
  --ink:#222222;
  --text:#555555;
  --muted:#7a7a7a;
  --light:#f2f2f2;
  --tint:#eef5fd;
  --white:#ffffff;
  --black:#000000;
}
*{margin:0;padding:0;box-sizing:border-box}
html,body{width:1200px;height:3864px;overflow:hidden}
body{position:relative;background:var(--white);font-family:'Barlow',sans-serif;color:var(--text)}
.abs{position:absolute}
h1,h2,h3{font-family:'Poppins',sans-serif;color:var(--ink)}
.rule{position:absolute;height:3px;width:60px;background:var(--blue)}
.btn{position:absolute;background:var(--blue);color:var(--white);font-family:'Poppins',sans-serif;font-weight:600;display:flex;align-items:center;justify-content:center;border-radius:2px}

/* header */
.site-header{position:absolute;left:0;top:0;width:1200px;height:68px;background:var(--white);border-bottom:1px solid #e6e6e6}
.brand{position:absolute;left:110px;top:21px;font-family:'Barlow',sans-serif;font-weight:600;font-size:21px;color:var(--ink)}
.nav a{position:absolute;top:24px;font-family:'Poppins',sans-serif;font-size:14px;color:var(--ink);text-decoration:none}
.nav a.active{color:var(--blue)}
.nav .underline{position:absolute;left:492px;top:64px;width:45px;height:3px;background:var(--blue)}

/* hero */
.hero{position:absolute;left:0;top:68px;width:1200px;height:642px;background:linear-gradient(110deg,#4b3a2c 0%,#8a7460 35%,#a08c76 55%,#6f5d4c 80%,#3e3128 100%)}
.hero-title{position:absolute;left:111px;font-size:88px;line-height:84px;font-weight:600;color:var(--white)}
.search{position:absolute;left:111px;top:655px;width:978px;height:130px;background:var(--light)}
.search label{position:absolute;top:25px;font-size:14px;color:#555}
.field{position:absolute;top:55px;height:40px;background:var(--white);border:1px solid #e3e3e3;font-size:13px;color:#666;display:flex;align-items:center;padding-left:18px;gap:7px}

/* about */
.about-photo{position:absolute;left:111px;top:888px;width:467px;height:443px;background:linear-gradient(135deg,#e9e9ea 0%,#cfd2d6 45%,#9aa0a8 75%,#5e5a52 100%)}
.about-title{position:absolute;left:633px;top:880px;font-size:40px;font-weight:600}
.about-text{position:absolute;left:633px;top:970px;width:454px;font-size:12.5px;line-height:21.4px;text-align:justify;color:var(--text)}
.about-text p+p{margin-top:21px}

/* category */
.category{position:absolute;left:0;top:1432px;width:1200px;height:488px;background:var(--light)}
.section-title{position:absolute;left:0;width:1200px;text-align:center;font-size:40px;font-weight:600}
.cat-card{position:absolute;top:200px;width:183px;height:185px;background:var(--white);box-shadow:0 2px 6px rgba(0,0,0,.06);text-align:center}
.cat-card svg{position:absolute;left:50%;top:36px;transform:translateX(-50%)}
.cat-card span{position:absolute;left:0;right:0;top:142px;font-size:17px;color:var(--ink)}
.circle-arrow{position:absolute;width:35px;height:35px;border:1.5px solid #777;border-radius:50%;display:flex;align-items:center;justify-content:center}

/* testimonials */
.quote-card{position:absolute;top:2139px;width:310px;height:236px;background:var(--tint)}
.quote-card svg{position:absolute;left:24px;top:-20px}
.quote-card p{position:absolute;left:28px;top:34px;width:256px;font-size:14px;line-height:21.5px;text-align:justify;color:#666}
.quote-card h3{position:absolute;left:28px;top:180px;font-family:'Barlow',sans-serif;font-weight:600;font-size:18px;color:#333}
.quote-card small{position:absolute;left:28px;top:207px;font-size:12px;color:#777}

/* donation */
.donation{position:absolute;left:0;top:2478px;width:1200px;height:452px;background:linear-gradient(120deg,#2b7acb 0%,#2574c2 50%,#2a78c6 100%)}
.donation h2{color:var(--white)}
.donation p{position:absolute;left:238px;top:160px;width:724px;text-align:center;font-size:14px;line-height:26px;color:var(--white)}
.partner{position:absolute;left:496px;top:280px;display:flex;align-items:center;gap:14px}
.partner .mark{width:62px;height:62px;background:rgba(255,255,255,.25)}
.partner span{font-family:'Barlow',sans-serif;font-weight:600;font-size:17px;line-height:18px;color:var(--white);width:150px}

/* newsletter */
.news-text{position:absolute;left:238px;top:3104px;width:724px;text-align:center;font-size:14px;line-height:26px;color:#666}
.news-form{position:absolute;left:291px;top:3187px;width:618px;height:53px;background:var(--light)}
.news-form span{position:absolute;left:25px;top:18px;font-size:14px;color:#777}

/* footer */
.site-footer{position:absolute;left:0;top:3342px;width:1200px;height:522px;background:var(--black);color:var(--white)}
.site-footer h3{position:absolute;font-family:'Barlow',sans-serif;font-weight:600;font-size:21px;color:var(--white)}
.links{position:absolute;left:181px;top:170px;list-style:none;font-size:14px;line-height:26px}
.links li::before{content:"»";margin-right:15px}
.vline{position:absolute;top:95px;width:1px;height:250px;background:#777}
.contact{position:absolute;left:412px;width:330px;text-align:center;font-size:14px;line-height:26px}
.dot{position:absolute;left:556px;width:40px;height:40px;border-radius:50%;background:var(--blue);display:flex;align-items:center;justify-content:center}
.social{position:absolute;top:470px;width:31px;height:31px;border:1.5px solid var(--white);border-radius:50%}
.copyright{position:absolute;left:0;top:424px;width:1200px;text-align:center;font-family:'Poppins',sans-serif;font-size:13px}
</style>
</head>
<body>

<header class="site-header">
  <div class="brand">Over Fence Hire</div>
  <nav class="nav">
    <a class="active" style="left:492px">Home</a>
    <a style="left:563px">About</a>
    <a style="left:633px">Contact</a>
    <a style="left:718px">Terms</a>
    <a style="left:789px">Privacy</a>
    <a style="left:868px">Services</a>
    <span class="underline"></span>
  </nav>
  <div class="btn" style="left:968px;top:16px;width:119px;height:36px;font-size:13px">Hire Out</div>
</header>

<section class="hero" role="img" aria-label="Worker in a hard hat and hi-vis vest climbing an aluminium ladder on a building site">
  <h1 class="hero-title" style="top:176px">Over Fence<br>Hire</h1>
  <div class="btn" style="left:114px;top:369px;width:118px;height:36px;font-size:13px">Hire Out</div>
</section>

<form class="search">
  <label style="left:28px">Location</label>
  <label style="left:264px">Type of Items</label>
  <label style="left:496px">Dates</label>
  <div class="field" style="left:29px;width:220px">
    <svg width="9" height="12" viewBox="0 0 9 12"><path d="M4.5 0A4.5 4.5 0 0 0 0 4.5C0 8 4.5 12 4.5 12S9 8 9 4.5A4.5 4.5 0 0 0 4.5 0zm0 6.2a1.7 1.7 0 1 1 0-3.4 1.7 1.7 0 0 1 0 3.4z" fill="#555"/></svg>Enter address</div>
  <div class="field" style="left:263px;width:220px">Items
    <svg style="position:absolute;right:16px" width="9" height="5" viewBox="0 0 9 5"><path d="M0 0h9L4.5 5z" fill="#444"/></svg></div>
  <div class="field" style="left:496px;width:220px">
    <svg width="12" height="12" viewBox="0 0 12 12"><rect x="0.5" y="1.5" width="11" height="10" fill="none" stroke="#666"/><path d="M0.5 4.5h11M3 0v3M9 0v3" stroke="#666"/></svg>Add date</div>
  <div class="btn" style="left:730px;top:55px;width:220px;height:40px;font-size:13px;gap:7px">
    <svg width="12" height="12" viewBox="0 0 12 12"><circle cx="5" cy="5" r="3.8" fill="none" stroke="#fff" stroke-width="1.8"/><path d="M8 8l3.3 3.3" stroke="#fff" stroke-width="2"/></svg>SEARCH</div>
</form>

<section class="about">
  <div class="abs" style="left:450px;top:836px;width:99px;height:172px;background:var(--blue)"></div>
  <div class="abs" style="left:84px;top:1192px;width:27px;height:100px;background:var(--blue)"></div>
  <div class="about-photo" role="img" aria-label="Worker carrying a step ladder up a staircase"></div>
  <h2 class="about-title">About Us</h2>
  <div class="rule" style="left:633px;top:942px"></div>
  <div class="about-text">
    <p>Lorem ipsum dolor sit amet, consectetur adipiscing elit, sed do eiusmod tempor incididunt ut labore et dolore magna aliqua. Ut enim ad minim veniam, quis nostrud exercitation ullamco laboris nisi ut aliquip ex ea commodo consequat. Duis aute irure dolor in reprehenderit in voluptate velit esse cillum dolore eu fugiat nulla pariatur.</p>
    <p>Excepteur sint occaecat cupidatat non proident, sunt in culpa qui officia deserunt mollit anim id est laborum. Lorem ipsum dolor sit amet, consectetur adipiscing elit, sed do eiusmod tempor incididunt ut labore et dolore magna aliqua. Ut enim ad minim veniam, quis nostrud exercitation ullamco laboris nisi ut aliquip ex ea commodo consequat. Duis aute irure dolor in reprehenderit in voluptate velit esse cillum dolore eu fugiat nulla pariatur. Excepteur sint occaecat cupidatat non proident, sunt in culpa qui officia deserunt mollit anim id est laborum.</p>
  </div>
  <div class="btn" style="left:635px;top:1289px;width:142px;height:41px;font-size:12px;gap:5px">LEARN MORE
    <svg width="11" height="11" viewBox="0 0 11 11"><circle cx="5.5" cy="5.5" r="5.5" fill="#fff"/><path d="M4.3 3l2.5 2.5-2.5 2.5" fill="none" stroke="#2a7bc8" stroke-width="1.6"/></svg></div>
</section>

<section class="category">
  <h2 class="section-title" style="top:95px">Our Category</h2>
  <div class="rule" style="left:570px;top:155px"></div>
  <div class="circle-arrow" style="left:38px;top:289px"><svg width="7" height="10" viewBox="0 0 7 10"><path d="M6 1L2 5l4 4" fill="none" stroke="#444" stroke-width="1.5"/></svg></div>
  <div class="circle-arrow" style="left:1127px;top:289px"><svg width="7" height="10" viewBox="0 0 7 10"><path d="M1 1l4 4-4 4" fill="none" stroke="#444" stroke-width="1.5"/></svg></div>

  <div class="cat-card" style="left:111px">
    <svg width="76" height="82" viewBox="0 0 76 82" fill="#2a7bc8"><path d="M36 0l42 8v74H36zM0 28h32v54H0z"/><g fill="#fff"><rect x="8" y="40" width="6" height="8"/><rect x="18" y="40" width="6" height="8"/><rect x="8" y="56" width="6" height="8"/><rect x="18" y="56" width="6" height="8"/><rect x="46" y="22" width="6" height="9"/><rect x="60" y="22" width="6" height="9"/><rect x="46" y="40" width="6" height="9"/><rect x="60" y="40" width="6" height="9"/><rect x="46" y="58" width="6" height="9"/><rect x="60" y="58" width="6" height="9"/></g></svg>
    <span>Building</span></div>
  <div class="cat-card" style="left:309px">
    <svg width="80" height="80" viewBox="0 0 80 80" fill="#2a7bc8"><path d="M6 14L14 6l14 10v6l34 34 10 0 8 10-10 12-10-8v-10L22 26h-6z"/><path d="M60 4a14 14 0 0 0-13 19L8 62a7 7 0 0 0 10 10l39-39A14 14 0 0 0 76 20l-9 9-9-3-3-9 9-9a14 14 0 0 0-4-4z"/></svg>
    <span>Tools</span></div>
  <div class="cat-card" style="left:508px">
    <svg width="96" height="78" viewBox="0 0 96 78" fill="#2a7bc8"><path d="M0 0h58v60H0z"/><path d="M62 18h18l16 20v22H62z"/><circle cx="18" cy="64" r="11" fill="#fff"/><circle cx="18" cy="64" r="7"/><circle cx="78" cy="64" r="11" fill="#fff"/><circle cx="78" cy="64" r="7"/><path d="M8 22h22v-10l16 18-16 18V38H8z" fill="#fff"/><path d="M12 26h22v-6l8 10-8 10v-6H12z"/><path d="M68 24h10l10 13H68z" fill="#fff"/></svg>
    <span>Moving</span></div>
  <div class="cat-card" style="left:707px">
    <svg width="92" height="80" viewBox="0 0 92 80" fill="#2a7bc8"><path d="M0 4h92v16H0z"/><path d="M6 20h10v60H6zM76 20h10v60H76zM24 20h7v34h-7zM61 20h7v34h-7z"/></svg>
    <span>Table</span></div>
  <div class="cat-card" style="left:905px">
    <svg width="92" height="86" viewBox="0 0 92 86" fill="#2a7bc8"><circle cx="46" cy="12" r="11"/><path d="M28 38a18 18 0 0 1 36 0z"/><circle cx="18" cy="54" r="10"/><path d="M0 86a18 18 0 0 1 36 0z"/><circle cx="74" cy="54" r="10"/><path d="M56 86a18 18 0 0 1 36 0z"/><path d="M36 64l8-6v4h4v-4l8 6-8 6v-4h-4v4z"/><path d="M18 38a28 28 0 0 1 10-18l3 4a22 22 0 0 0-7 14zM74 38a28 28 0 0 0-10-18l-3 4a22 22 0 0 1 7 14z"/></svg>
    <span>Party Hire</span></div>
</section>

<section class="testimonials">
  <h2 class="section-title" style="top:2010px">Our Testimonials</h2>
  <div class="rule" style="left:570px;top:2072px"></div>
  <svg class="abs" style="left:50px;top:2245px" width="12" height="18" viewBox="0 0 12 18"><path d="M10 1L2 9l8 8" fill="none" stroke="#333" stroke-width="2"/></svg>
  <svg class="abs" style="left:1138px;top:2245px" width="12" height="18" viewBox="0 0 12 18"><path d="M2 1l8 8-8 8" fill="none" stroke="#333" stroke-width="2"/></svg>

  <article class="quote-card" style="left:111px">
    <svg width="40" height="36" viewBox="0 0 40 36" fill="#2a7bc8"><path d="M2 36V20C2 10 7 3 16 0l2 4C12 7 10 12 10 18h7v18zM22 36V20C22 10 27 3 36 0l2 4C32 7 30 12 30 18h7v18z"/></svg>
    <p>Lorem ipsum dolor sit amet, consectetur adipiscing elit, sed do eiusmod tempor incididunt ut labore et dolore magna aliqua. Ut enim ad minim veniam, quis nostrud exercitation ullamco laboris nisi ut aliquip ex ea commodo consequat</p>
    <h3>John Doe</h3><small>Company name</small>
  </article>
  <article class="quote-card" style="left:445px">
    <svg width="40" height="36" viewBox="0 0 40 36" fill="#2a7bc8"><path d="M2 36V20C2 10 7 3 16 0l2 4C12 7 10 12 10 18h7v18zM22 36V20C22 10 27 3 36 0l2 4C32 7 30 12 30 18h7v18z"/></svg>
    <p>Lorem ipsum dolor sit amet, consectetur adipiscing elit, sed do eiusmod tempor incididunt ut labore et dolore magna aliqua. Ut enim ad minim veniam, quis nostrud exercitation ullamco laboris nisi ut aliquip ex ea commodo consequat</p>
    <h3>John Doe</h3><small>Company name</small>
  </article>
  <article class="quote-card" style="left:778px">
    <svg width="40" height="36" viewBox="0 0 40 36" fill="#2a7bc8"><path d="M2 36V20C2 10 7 3 16 0l2 4C12 7 10 12 10 18h7v18zM22 36V20C22 10 27 3 36 0l2 4C32 7 30 12 30 18h7v18z"/></svg>
    <p>Lorem ipsum dolor sit amet, consectetur adipiscing elit, sed do eiusmod tempor incididunt ut labore et dolore magna aliqua. Ut enim ad minim veniam, quis nostrud exercitation ullamco laboris nisi ut aliquip ex ea commodo consequat</p>
    <h3>John Doe</h3><small>Company name</small>
  </article>
</section>

<section class="donation" role="img" aria-label="Blue-tinted photo of a community workshop interior">
  <h2 class="section-title" style="top:70px">Donation</h2>
  <div class="rule" style="left:570px;top:132px;background:var(--white)"></div>
  <p>Lorem ipsum dolor sit amet, consectetur adipiscing elit, sed do eiusmod tempor incididunt ut labore et dolore magna aliqua. Ut enim ad minim veniam, quis nostrud exercitation ullamco laboris nisi ut aliquip ex ea commodo consequat. Lorem ipsum dolor sit amet, consectetur adipiscing elit, sed do eiusmod tempor incididunt ut labore et dolore magna aliqua. Ut enim ad minim veniam, quis nostrud exercitation ullamco laboris</p>
  <div class="partner"><div class="mark"></div><span>Regional Workshop Collective</span></div>
</section>

<section class="newsletter">
  <h2 class="section-title" style="top:3012px">Subscribe to Our Newsletter</h2>
  <div class="rule" style="left:570px;top:3075px"></div>
  <p class="news-text">Lorem ipsum dolor sit amet, consectetur adipiscing elit, sed do eiusmod tempor incididunt ut labore et dolore magna aliqua. Ut enim ad minim veniam, quis nostrud exercitation ullamco laboris</p>
  <div class="news-form"><span>Email address</span>
    <div class="btn" style="left:457px;top:5px;width:154px;height:43px;font-size:13px">SUBSCRIBE</div></div>
</section>

<footer class="site-footer">
  <h3 style="left:181px;top:110px">QUICK LINKS</h3>
  <ul class="links">
    <li>Home</li><li>About Us</li><li>Payment Terms</li><li>Hire Aggreement</li><li>Public Liablity</li><li>Insurance Coverage</li>
  </ul>
  <div class="vline" style="left:383px"></div>
  <div class="vline" style="left:777px"></div>

  <div class="dot" style="top:75px"><svg width="9" height="12" viewBox="0 0 9 12"><path d="M4.5 0A4.5 4.5 0 0 0 0 4.5C0 8 4.5 12 4.5 12S9 8 9 4.5A4.5 4.5 0 0 0 4.5 0zm0 6.2a1.7 1.7 0 1 1 0-3.4 1.7 1.7 0 0 1 0 3.4z" fill="#fff"/></svg></div>
  <div class="contact" style="top:124px">123, Lorem ipsum dolor sit amet,<br>consectetur adipiscing eli</div>
  <div class="dot" style="top:178px"><svg width="13" height="10" viewBox="0 0 13 10"><rect width="13" height="10" fill="#fff"/><path d="M0 0l6.5 5L13 0" fill="none" stroke="#2a7bc8" stroke-width="1.3"/></svg></div>
  <div class="contact" style="top:228px">info@companyname.com</div>
  <div class="dot" style="top:264px"><svg width="12" height="12" viewBox="0 0 12 12"><path d="M2.5 0l2 3-1.3 1.5a7 7 0 0 0 4.3 4.3L9 7.5l3 2-1.5 2.5C5 12 0 7 0 1.5z" fill="#fff"/></svg></div>
  <div class="contact" style="top:314px">+1 888 888 8888</div>

  <h3 style="left:833px;top:110px">NEWSLETTER</h3>
  <p class="abs" style="left:833px;top:160px;width:270px;font-size:14px;line-height:26px">Lorem ipsum dolor sit amet, consectetur adipiscing elit, sed do eiusmod tempor</p>
  <div class="abs" style="left:835px;top:233px;width:247px;height:44px;background:var(--white)">
    <span class="abs" style="left:24px;top:13px;font-size:14px;color:#777">Email address</span>
    <div class="abs" style="left:204px;top:5px;width:37px;height:34px;background:var(--blue);display:flex;align-items:center;justify-content:center">
      <svg width="14" height="13" viewBox="0 0 14 13"><path d="M0 6L14 0 11 13 7 9 5 12V8l7-6-8 5z" fill="#fff"/></svg></div>
  </div>

  <div class="abs" style="left:111px;top:392px;width:978px;height:1px;background:#666"></div>
  <p class="copyright">© Copyrights 2023 Company Name | All Rights reserved</p>
  <div class="social" style="left:527px"></div>
  <div class="social" style="left:561px"></div>
  <div class="social" style="left:595px"></div>
  <div class="social" style="left:629px"></div>
</footer>

</body>
</html>
```